Health care product retail website

We need a website design for a company based in New Zealand that sells fresh air to an overseas market.
There are 4 products to start with and we have a logo. We need to give the message that it is unpolluted and clean. We are also promoting a self-sustaining business model by investing in the planet's future. The website will be developed in WordPress and if you can suggest coding thats a bonus, but not necessary as I can develop in Wordpress.

Target Market(s)

Chinese, Indian, Middle Eastern or anywhere where the air is quite polluted. middle-income target market

Industry/Entity Type

Health And Wellness

Number of Pages Required

5+ page

Font styles to use
Sans Serif

Requirements
Must have
• Homepage: Clean, fresh look. Indicate that the product is sourced and bottled in a clean environment.
• Any help with e-commerce and multilingual pages appreciated.
• Home, Products, Our locations, Environmental protection, Science

```html
<!DOCTYPE html>
<html lang="en">
<head>
<meta charset="utf-8">
<title>Kaimai Clear Air</title>
<link href="https://fonts.googleapis.com/css2?family=Lato:ital,wght@0,300;0,400;0,700;1,400;1,700&display=swap" rel="stylesheet">
<style>
:root{
  --green:#8cc63f;
  --blue:#1fa8e4;
  --blue-dark:#0f73a5;
  --grey-bg:#eeeff1;
  --line:#d6d8db;
  --text:#8a8d91;
  --heading:#666a6e;
  --dark:#4a4d50;
  --white:#ffffff;
}
*{margin:0;padding:0;box-sizing:border-box}
html,body{width:1200px;height:2620px;overflow:hidden;background:var(--white)}
body{position:relative;font-family:"Lato",Arial,sans-serif;color:var(--text)}
.abs{position:absolute}

/* header */
.phone-tab{left:0;top:0;width:380px;height:65px}
.phone-text{left:88px;top:22px;color:var(--white);font-size:14px;font-weight:700}
.top-links{top:14px;left:480px;display:flex;align-items:center;gap:30px;font-size:16px;color:var(--green)}
.top-links .item{display:flex;align-items:center;gap:6px}
.login{left:926px;top:23px;font-size:16px;color:var(--green)}
.login em{font-style:normal;color:#aaa;margin:0 14px}
.join{left:1018px;top:16px;width:136px;height:38px;background:var(--green);color:var(--white);font-weight:700;font-size:16px;display:flex;align-items:center;justify-content:center;border-radius:2px}
.nav-band{left:355px;top:65px;width:845px;height:66px}
.main-nav{left:481px;top:89px;display:flex;gap:14px;color:var(--white);font-size:16px;text-transform:uppercase}
.logo-panel{left:0;top:65px;width:380px;height:124px;z-index:3}
.brand{left:48px;top:112px;z-index:4;display:flex;align-items:center;gap:10px;color:var(--green);font-weight:700;font-size:26px;line-height:1}
.brand i{display:block;width:22px;height:22px;border-radius:50%;background:var(--green)}

/* hero */
.hero{left:0;top:131px;width:1200px;height:589px;background:linear-gradient(180deg,#6fa6d8 0%,#a9cde8 26%,#3f8d96 38%,#2f6e33 55%,#1f4a1c 78%,#2b5a22 100%)}
.hero-title{left:0;top:350px;width:1200px;text-align:center;font-size:45px;font-weight:300;color:var(--white);letter-spacing:1px;text-shadow:0 1px 3px rgba(0,0,0,.3)}
.hero-title b{font-weight:300;color:var(--green)}
.hero-rule{top:378px;height:2px;background:rgba(255,255,255,.85)}
.dots{left:551px;top:689px;display:flex;gap:6px}
.dots i{display:block;width:28px;height:6px;border-radius:3px;background:var(--white)}
.dots i:first-child{background:var(--green)}

/* about */
.about{left:0;top:720px;width:1200px;height:777px;background:var(--grey-bg)}
.sec-rule{height:1px;background:var(--line)}
.sec-title{font-size:24px;color:var(--heading);background:var(--grey-bg);padding:0 16px;letter-spacing:1px}
.about-body{left:91px;top:800px;width:1016px}
.about-body h2{font-size:21px;font-weight:700;color:var(--heading);margin:0 0 8px}
.about-body p{font-size:15.5px;line-height:28.5px;font-weight:300;margin-bottom:20px}

/* arrivals */
.arrival-title{left:0;top:1524px;width:1200px;text-align:center;font-size:25px;color:var(--heading)}
.arrival-title .l{color:#999}
.arrival-title .r{color:var(--blue)}
.card{top:1586px;width:260px;height:362px;border:1px solid #dfe1e3;background:var(--white)}
.card.active{border:2px solid #b6dbef}
.tag{position:absolute;left:22px;top:-9px;width:216px;height:60px}
.tag .name{position:absolute;left:0;top:16px;width:216px;text-align:center;color:var(--white);font-style:italic;font-weight:700;font-size:15px}
.tag .price{position:absolute;left:0;top:40px;width:216px;text-align:center;color:var(--white);font-weight:700;font-size:13px}
.tag s{margin-right:14px}
.bottle{position:absolute;left:95px;top:92px;width:70px;height:220px;border-radius:14px 14px 8px 8px}
.b1{background:linear-gradient(180deg,#f2f2f2,#d9cde6 60%,#b8a7cf)}
.b2{background:linear-gradient(180deg,#cfcfd6,#8063c4 40%,#5b3fa6)}
.b3{background:linear-gradient(180deg,#e8eef3,#8fc2e2 50%,#5da4d3)}
.b4{left:100px;top:165px;width:62px;height:120px;border-radius:30px 30px 10px 10px;background:linear-gradient(180deg,#f4f4f4,#c9c9c9)}
.badge{position:absolute;top:283px;width:44px;height:44px;border-radius:50%;background:var(--green);color:var(--white);font-size:11px;display:flex;align-items:center;justify-content:center}
.slider-line{left:70px;top:1987px;width:1060px;height:2px;background:var(--green)}
.slider-dots{left:540px;top:1979px;display:flex;gap:4px}
.slider-dots i{display:block;width:18px;height:18px;border-radius:50%;border:2px solid var(--green);background:var(--white)}
.slider-dots i:first-child{background:var(--green)}

/* contact */
.contact-tab{left:468px;top:2040px;width:262px;height:48px}
.contact-label{left:468px;top:2050px;width:262px;text-align:center;color:var(--white);font-size:26px}
.contact{left:0;top:2087px;width:1200px;height:320px;background:var(--grey-bg)}
.col-title{font-size:17px;color:var(--green)}
.address{left:48px;top:2150px;font-size:14px;color:var(--dark);line-height:30px}
.address .row{display:flex;align-items:center;gap:14px}
.socials{left:48px;top:2279px;display:flex;gap:26px}
.socials i{display:block;width:20px;height:20px;border-radius:3px;background:var(--dark)}
.form{left:328px;top:2150px;width:380px}
.field{position:absolute;left:0;font-size:15px;font-style:italic;color:#666;width:380px}
.field .input{position:absolute;left:80px;width:300px;border-bottom:1px solid #9a9c9f;text-align:center;font-size:12px;color:#777;padding-bottom:3px}
.send{left:664px;top:2368px;color:var(--green);font-size:16px;text-decoration:underline}
.map{left:803px;top:2160px;width:252px;height:198px;border:4px solid var(--green);background:linear-gradient(135deg,#f2e9c8,#e6dfc7 40%,#d7e4cc 70%,#f0e4bd)}

/* footer */
.footer{left:0;top:2407px;width:1200px;height:213px;background:var(--blue)}
.f-col{top:2429px;color:var(--white);font-size:15px;line-height:26px}
.f-col h3{font-size:16px;font-weight:700;margin-bottom:4px}
.f-brand{left:690px;top:2475px;display:flex;align-items:center;gap:10px;color:var(--white);font-weight:700;font-size:22px}
.f-brand i{display:block;width:18px;height:18px;border-radius:50%;background:var(--white)}
.copy{left:668px;top:2543px;width:250px;text-align:center;color:var(--white);font-size:13px;font-weight:700;line-height:22px}
.pay{left:944px;display:flex;align-items:center;gap:8px;color:var(--white);font-weight:700;font-size:15px}
.pay i{display:block;width:14px;height:14px;background:var(--white)}
</style>
</head>
<body>

<!-- header -->
<svg class="abs phone-tab" viewBox="0 0 380 65" aria-hidden="true"><polygon points="0,0 380,0 335,65 0,65" fill="#8cc63f"/>
  <circle cx="34" cy="30" r="18" fill="#fff"/>
  <path d="M27 24c1-2 3-2 4 0l1 3c0 1-1 2-2 2 1 3 3 5 6 6 0-1 1-2 2-2l3 1c2 1 2 3 0 4-5 3-15-7-14-14z" fill="#8cc63f"/></svg>
<div class="abs phone-text">555-010-2040 (For Support )</div>

<div class="abs top-links">
  <div class="item"><svg width="30" height="30" viewBox="0 0 30 30"><circle cx="15" cy="15" r="13" fill="none" stroke="#8cc63f" stroke-width="2"/><path d="M8 10h3l2 8h8l2-6H12" fill="none" stroke="#8cc63f" stroke-width="2"/><circle cx="14" cy="21" r="1.5" fill="#8cc63f"/><circle cx="20" cy="21" r="1.5" fill="#8cc63f"/></svg>My Cart</div>
  <div class="item"><svg width="30" height="30" viewBox="0 0 30 30"><circle cx="15" cy="15" r="13" fill="#8cc63f"/><circle cx="15" cy="11" r="4" fill="#fff"/><path d="M8 22c1-5 13-5 14 0z" fill="#fff"/></svg>My Account</div>
  <div class="item"><svg width="26" height="30" viewBox="0 0 26 30"><rect x="2" y="3" width="22" height="25" rx="2" fill="none" stroke="#8cc63f" stroke-width="2"/><path d="M13 22l-5-5c-2-2 0-5 2-5 1 0 2 1 3 2 1-1 2-2 3-2 2 0 4 3 2 5z" fill="#8cc63f"/></svg>My Wish List</div>
</div>
<div class="abs login">Log In<em>or</em></div>
<div class="abs join">JOIN NOW</div>

<svg class="abs nav-band" viewBox="0 0 845 66" aria-hidden="true"><polygon points="60,0 845,0 845,66 0,66" fill="#8cc63f"/></svg>
<nav class="abs main-nav"><span>Home</span><span>Our Products</span><span>Our Locations</span><span>Environmental Protection</span><span>Science</span></nav>

<!-- hero -->
<div class="abs hero" role="img" aria-label="Coastal landscape with turquoise bay, islands and green forested hills"></div>
<svg class="abs logo-panel" viewBox="0 0 380 124" aria-hidden="true"><polygon points="0,0 290,0 375,66 345,124 0,124" fill="#fff"/></svg>
<div class="abs brand"><i></i>Kaimai Clear Air</div>

<div class="abs hero-rule" style="left:138px;width:72px"></div>
<div class="abs hero-rule" style="left:990px;width:72px"></div>
<div class="abs hero-title"><b>FRESH AIR</b> IMPROVISES DOCTOR</div>
<svg class="abs" style="left:48px;top:350px" width="32" height="60" viewBox="0 0 32 60"><path d="M28 2L4 30l24 28" fill="none" stroke="#fff" stroke-width="3"/></svg>
<svg class="abs" style="left:1120px;top:350px" width="32" height="60" viewBox="0 0 32 60"><path d="M4 2l24 28L4 58" fill="none" stroke="#fff" stroke-width="3"/></svg>
<div class="abs dots"><i></i><i></i><i></i></div>

<!-- about -->
<section class="abs about"></section>
<div class="abs sec-rule" style="left:48px;top:768px;width:1104px"></div>
<div class="abs sec-title" style="left:520px;top:750px">ABOUT US</div>
<div class="abs about-body">
  <h2>What is Lorem Ipsum ...?</h2>
  <p>Lorem Ipsum is slechts een proeftekst uit het drukkerij- en zetterijwezen. Lorem Ipsum is de standaard proeftekst in deze bedrijfstak sinds de 16e eeuw, toen een onbekende drukker een zethaak met letters nam en ze door elkaar husselde om een font-catalogus te maken. Het heeft niet alleen vijf eeuwen overleefd maar is ook, vrijwel onveranderd, overgenomen in elektronische letterzetting. Het is in de jaren '60 populair geworden met de introductie van overdrukvellen met Lorem Ipsum passages en meer recentelijk door moderne opmaaksoftware die versies van Lorem Ipsum bevatten.</p>
  <h2>Why is Lorem Ipsum ...?</h2>
  <p>In tegenstelling tot wat algemeen aangenomen wordt is Lorem Ipsum niet zomaar willekeurige tekst. het heeft zijn wortels in een stuk klassieke latijnse literatuur uit 45 v.Chr. en is dus meer dan 2000 jaar oud. Een professor latijn aan een college heeft één van de meer obscure latijnse woorden, consectetur, uit een Lorem Ipsum passage opgezocht, en heeft tijdens het zoeken naar het woord in de klassieke literatuur de onverdachte bron ontdekt. Lorem Ipsum komt uit de secties 1.10.32 en 1.10.33 van een oud filosofisch werk over goed en kwaad, geschreven in 45 v.Chr. Dit boek is een verhandeling over de theorie der ethiek, erg populair tijdens de renaissance. De eerste regel van Lorem Ipsum, "Lorem ipsum dolor sit amet..", komt uit een zin in sectie</p>
  <h2>How is Lorem Ipsum ...?</h2>
  <p>Er zijn vele variaties van passages van Lorem Ipsum beschikbaar maar het merendeel heeft te lijden gehad van wijzigingen in een of andere vorm, door ingevoegde humor of willekeurig gekozen woorden die nog niet half geloofwaardig ogen. Als u een passage uit Lorum Ipsum gaat gebruiken dient u zich ervan te verzekeren dat er niets beschamends midden in de tekst verborgen zit. Alle Lorum Ipsum generators op Internet hebben de eigenschap voorgedefinieerde stukken te herhalen waar nodig zodat dit de eerste echte generator is op internet. Het gebruik een woordenlijst van 200 latijnse woorden gecombineerd met een handvol zinsstructuur modellen om een Lorum Ipsum te genereren die redelijk overkomt. De gegenereerde Lorum Ipsum is daardoor altijd vrij van herhaling, ingevoegde humor of ongebruikelijke woorden etc</p>
</div>
<div class="abs sec-rule" style="left:91px;top:1460px;width:1016px"></div>

<!-- new arrival -->
<div class="abs arrival-title"><span class="l">‹</span> NEW ARRIVAL <span class="r">›</span></div>

<div class="abs card active" style="left:47px">
  <svg class="tag" viewBox="0 0 216 60" aria-hidden="true"><polygon points="0,0 206,0 216,9 216,60 0,60" fill="#1fa8e4"/><polygon points="206,0 216,9 206,9" fill="#0f73a5"/></svg>
  <div class="tag"><div class="name">Lorem Ipsum</div><div class="price"><s>NZ $30.00</s>NZ $25.00</div></div>
  <div class="bottle b1" role="img" aria-label="Lavender air spray bottle"></div>
  <div class="badge" style="left:36px">4.5/5</div>
  <div class="badge" style="left:107px"><svg width="24" height="20" viewBox="0 0 24 20"><path d="M1 2h4l3 10h11l3-8H7" fill="none" stroke="#fff" stroke-width="2"/><circle cx="10" cy="17" r="2" fill="#fff"/><circle cx="18" cy="17" r="2" fill="#fff"/></svg></div>
  <div class="badge" style="left:176px"><svg width="20" height="18" viewBox="0 0 20 18"><path d="M10 17L2 9C-1 6 2 1 6 2c2 0 3 2 4 3 1-1 2-3 4-3 4-1 7 4 4 7z" fill="#fff"/></svg></div>
</div>
<div class="abs card" style="left:330px">
  <svg class="tag" viewBox="0 0 216 60" aria-hidden="true"><polygon points="0,0 206,0 216,9 216,60 0,60" fill="#1fa8e4"/><polygon points="206,0 216,9 206,9" fill="#0f73a5"/></svg>
  <div class="tag"><div class="name">Lorem</div><div class="price">NZ $25.00</div></div>
  <div class="bottle b2" role="img" aria-label="Purple trigger spray bottle"></div>
</div>
<div class="abs card" style="left:611px">
  <svg class="tag" viewBox="0 0 216 60" aria-hidden="true"><polygon points="0,0 206,0 216,9 216,60 0,60" fill="#1fa8e4"/><polygon points="206,0 216,9 206,9" fill="#0f73a5"/></svg>
  <div class="tag"><div class="name">Lorem Ipsum Again</div><div class="price">NZ $45.00</div></div>
  <div class="bottle b3" role="img" aria-label="Light blue pump bottle"></div>
</div>
<div class="abs card" style="left:893px">
  <svg class="tag" viewBox="0 0 216 60" aria-hidden="true"><polygon points="0,0 206,0 216,9 216,60 0,60" fill="#1fa8e4"/><polygon points="206,0 216,9 206,9" fill="#0f73a5"/></svg>
  <div class="tag"><div class="name">Lorem Ipsum Once Again</div><div class="price">NZ $15.00</div></div>
  <div class="bottle b4" role="img" aria-label="Small white air diffuser"></div>
</div>

<div class="abs slider-line"></div>
<svg class="abs" style="left:44px;top:1962px" width="52" height="52" viewBox="0 0 52 52"><rect x="11" y="11" width="30" height="30" transform="rotate(45 26 26)" fill="#fff" stroke="#8cc63f" stroke-width="2"/><path d="M30 18l-8 8 8 8" fill="none" stroke="#8cc63f" stroke-width="2"/></svg>
<svg class="abs" style="left:1100px;top:1962px" width="52" height="52" viewBox="0 0 52 52"><rect x="11" y="11" width="30" height="30" transform="rotate(45 26 26)" fill="#fff" stroke="#8cc63f" stroke-width="2"/><path d="M22 18l8 8-8 8" fill="none" stroke="#8cc63f" stroke-width="2"/></svg>
<div class="abs slider-dots"><i></i><i></i><i></i></div>

<!-- contact -->
<section class="abs contact"></section>
<svg class="abs contact-tab" viewBox="0 0 262 48" aria-hidden="true"><polygon points="16,0 262,0 246,48 0,48" fill="#8cc63f"/></svg>
<div class="abs contact-label">CONTACT US</div>

<div class="abs col-title" style="left:103px;top:2105px">Address</div>
<div class="abs address">
  <div class="row"><svg width="12" height="12" viewBox="0 0 12 12"><path d="M11 1L1 5l5 1 1 5z" fill="#333"/></svg>Kaimai Clear Air</div>
  <div class="row" style="padding-left:26px">14 Fernleaf Lane</div>
  <div class="row"><svg width="14" height="11" viewBox="0 0 14 11"><rect x="1" y="1" width="12" height="9" fill="none" stroke="#333"/><path d="M1 1l6 5 6-5" fill="none" stroke="#333"/></svg>hello@kaimaiclear.example</div>
  <div class="row"><svg width="14" height="14" viewBox="0 0 14 14"><rect x="4" y="1" width="6" height="12" rx="1" fill="none" stroke="#333" stroke-width="1.4"/></svg>800-555-0199</div>
</div>
<div class="abs socials"><i></i><i></i><i></i><i></i></div>

<div class="abs col-title" style="left:499px;top:2105px">Keep In Touch</div>
<div class="abs form">
  <div class="field" style="top:0">Name :<div class="input" style="top:-2px">Your Name</div></div>
  <div class="field" style="top:37px">E-mail :<div class="input" style="top:-2px">Your Mail</div></div>
  <div class="field" style="top:74px">Number :<div class="input" style="top:-2px">Your Contact Number</div></div>
  <div class="field" style="top:111px">Message :<div class="input" style="top:75px">Your Feedback</div></div>
</div>
<div class="abs send">SEND</div>

<div class="abs col-title" style="left:945px;top:2105px">Find Us</div>
<div class="abs map" role="img" aria-label="Street map showing the company location"></div>

<!-- footer -->
<footer class="abs footer"></footer>
<div class="abs f-col" style="left:163px"><h3>QUICK LINKS</h3>Home<br>Our Products<br>Our locations<br>Environmental protection<br>Science</div>
<div class="abs f-col" style="left:435px"><h3>CUSTOMER SERVICE</h3>Customer Service<br>Privacy Policy<br>Orders and Returns<br>Shipping Information<br>Our Staff Members</div>
<div class="abs f-brand"><i></i>Kaimai Clear Air</div>
<div class="abs copy">© 2016 Kaimai Clear Air<br>All Rights Reserved.</div>
<div class="abs pay" style="top:2452px"><i></i>Tovapay</div>
<div class="abs pay" style="top:2500px"><i></i>Norvo</div>
<div class="abs pay" style="top:2552px"><i></i>Quillcard</div>

</body>
</html>
```